" Um café onde o croissant é o produto carro chefe. Um local para um lanche rápido, com arquitetura premium e minimalista. Croissants especiais, produto premium, com receita francesa, e recheios salgados e doces. Além disso, temos cafés especiais para acompanhar os croissants. Um momento de indulgência no meio de um dia corrido. "

```html
<!DOCTYPE html>
<html lang="pt">
<head>
<meta charset="utf-8">
<title>Maison Brûlé — Envelopes</title>
<link rel="stylesheet" href="https://fonts.googleapis.com/css2?family=Josefin+Sans:wght@300&display=swap">
<style>
  :root {
    --backdrop: #ecebe8;
    --paper: #ffffff;
    --ink: #0b0b0b;
    --gold-dark: #a8792e;
    --gold-light: #e9c77d;
    --logo-grey: #5a5a5a;
    --window-line: #c9c9c9;
  }
  html, body {
    margin: 0;
    padding: 0;
    width: 1200px;
    height: 1200px;
    overflow: hidden;
    background: var(--backdrop);
  }
  .canvas {
    position: relative;
    width: 1200px;
    height: 1200px;
  }
  .envelope {
    position: absolute;
    left: 197px;
    width: 782px;
  }
  .envelope--front { top: 29px; height: 607px; }
  .envelope--back { top: 708px; height: 444px; }
  .envelope svg {
    position: absolute;
    inset: 0;
    width: 100%;
    height: 100%;
    filter: drop-shadow(0 8px 10px rgba(0,0,0,0.18));
  }
  .brand-name {
    position: absolute;
    right: 90px;
    top: 280px;
    margin: 0;
    font-family: "Josefin Sans", sans-serif;
    font-weight: 300;
    font-size: 36px;
    letter-spacing: 2px;
    color: var(--logo-grey);
    white-space: nowrap;
    line-height: 1;
  }
  .address-window {
    position: absolute;
    left: 67px;
    top: 458px;
    width: 420px;
    height: 96px;
    border: 2px solid var(--window-line);
    border-radius: 14px;
    box-sizing: border-box;
  }
</style>
</head>
<body>
<main class="canvas">

  <section class="envelope envelope--front" aria-label="Frente do envelope">
    <svg viewBox="0 0 782 607" preserveAspectRatio="none" aria-hidden="true">
      <defs>
        <linearGradient id="gold" x1="0" y1="0" x2="1" y2="0">
          <stop offset="0" stop-color="#a8792e"/>
          <stop offset="0.45" stop-color="#e9c77d"/>
          <stop offset="1" stop-color="#a8792e"/>
        </linearGradient>
      </defs>
      <rect class="envelope-body" x="0" y="90" width="782" height="517" fill="var(--paper)"/>
      <path class="envelope-flap"
            d="M0 170 L0 96 Q0 88 10 84 L120 12 Q132 0 150 0 L632 0 Q650 0 662 12 L772 84 Q782 88 782 96 L782 170 Z"
            fill="var(--ink)"/>
      <rect class="gold-band" x="0" y="170" width="782" height="10" fill="url(#gold)"/>
      <rect class="gold-rule" x="0" y="187" width="782" height="4" fill="url(#gold)"/>
    </svg>
    <p class="brand-name">MAISON BRÛLÉ</p>
    <div class="address-window"></div>
  </section>

  <section class="envelope envelope--back" aria-label="Verso do envelope">
    <svg viewBox="0 0 782 444" preserveAspectRatio="none" aria-hidden="true">
      <rect class="envelope-body" x="0" y="0" width="782" height="444" fill="var(--paper)" rx="3"/>
      <path class="envelope-flap"
            d="M0 0 L782 0 L782 72 Q782 90 764 96 L410 142 Q391 146 372 142 L18 96 Q0 90 0 72 Z"
            fill="var(--ink)"/>
    </svg>
  </section>

</main>
</body>
</html>
```